【概要】 求人サイトに掲載するサムネイル画像作成依頼です。 素敵なデザインがあれば複数採用いたします。 【 依頼内容 】 ・サイズ:横900x縦600 ・ターゲット:20代~50代向けの求人 【 入れていただきたい文言】※これ以外の文言は入れないでください ・固定ルート+体力負担なし+無理な運転はさせない社風=長く働ける環境です! ・6tドライバー募集 ・月給35万円可能 【画像に関して】 注:こちらの画像サイズ、データで提出できる方のみお願い致します。 ★「横900ピクセルx縦600ピクセル」(PNGファイル×1、PSDデータ×1) ・配信時は制作したバナーがスマホの画面幅程度に縮小されて表示されます。テキストの可読性を考慮して制作お願いします。 ・文字を記入する際、できれば画像としてではなく、フォトショップのテキストを使用していただければと存じます。 ・テキストデータはアウトライン化されていない、後から編集できる状態での納品をお願いいたします。(イラストレーターNG) ・フォントやあしらいにフリー素材を使用する場合は著作権に抵触しないものをご利用下さい。 【重要な指定】 ※目を惹きクリックされるインパクトのあるバナーをお願い致します。 サイト内で使用するものなので「こちらをクリック」「詳細はこちら」などのフレーズはなしでお願いいたします。 ・添付画像をご使用ください ・添付画像は反転しないで下さい 【ご注意】 ※他で登録されているデザインや商標の転用など、他社の知的財産権を侵すことNG ※他のクライアントへ既に提案した内容の転用などNG ※ご提案頂きましたバナー案について、SNSへの投稿・Webサイトへのアップ等NG →ポートフォリオ・コンペ提案作品一覧にもアップNGです。 アップする際には、社名を削除し、写真はフリー素材に差し替えてください。 ※今後、画像を再利用する可能性がございます。 ※WEBサイトで他の求人に使用することがあります。 【対応時間】 平日:9時半~18時半 その他ご質問、ご不明点等ありましたら、気軽にお問い合わせください。 見やすく、素敵なデザインをお待ちしております! |
どの案も素敵でしたが、こちらの作品が一番イメージに合っておりました。
皆様ご提案ありがとうございました。どれも個性的でよい提案ばかりでした。また機会がありましたら依頼させていただきますのでよろしくお願いします。

```html
<!DOCTYPE html>
<html lang="ja">
<head>
<meta charset="utf-8">
<title>6tドライバー募集</title>
<link href="https://fonts.googleapis.com/css2?family=Noto+Sans+JP:wght@700;900&family=Shippori+Mincho+B1:wght@800&display=swap" rel="stylesheet">
<style>
  :root{
    --navy:#1d3a78;
    --navy-dark:#142a5a;
    --red:#d8141c;
    --gold:#f2c94c;
    --gold-deep:#c9961e;
    --ink:#111;
    --white:#fff;
  }
  html,body{margin:0;padding:0;overflow:hidden;}
  .banner{
    position:relative;width:1200px;height:800px;overflow:hidden;
    font-family:"Noto Sans JP",sans-serif;color:var(--ink);
  }
  .photo{
    position:absolute;inset:0;
    background:
      radial-gradient(ellipse at 50% 35%, #e9ecef 0%, #b9c0c8 35%, transparent 60%),
      linear-gradient(90deg,#6d747c 0%,#9aa2aa 25%,#cfd4d9 50%,#8e959c 78%,#5e646b 100%);
  }
  .pill{
    position:absolute;background:var(--white);border-radius:18px;
    box-shadow:0 3px 8px rgba(0,0,0,.35);
    display:flex;align-items:center;justify-content:center;text-align:center;
    font-weight:900;font-size:34px;line-height:1.25;
  }
  .pill--route{left:54px;top:58px;width:256px;height:96px;}
  .pill--stamina{left:34px;top:246px;width:268px;height:96px;}
  .pill--culture{left:34px;top:460px;width:290px;height:120px;font-size:30px;}
  .op{
    position:absolute;color:var(--white);font-weight:900;font-size:72px;line-height:1;
    text-shadow:0 2px 6px rgba(0,0,0,.5);
  }
  .op--plus1{left:146px;top:164px;}
  .op--plus2{left:146px;top:370px;}
  .op--eq{left:344px;top:484px;}
  .bubble{position:absolute;left:0;top:0;width:1200px;height:800px;pointer-events:none;}
  .bubble-text{
    position:absolute;left:420px;top:444px;width:520px;height:166px;
    display:flex;flex-direction:column;justify-content:center;
    font-weight:900;font-size:52px;line-height:1.2;padding-left:30px;box-sizing:border-box;
  }
  .bubble-text span:last-child{padding-left:150px;}
  .headline{
    position:absolute;color:var(--red);font-weight:900;
    -webkit-text-stroke:8px var(--white);paint-order:stroke fill;
    text-shadow:0 4px 10px rgba(0,0,0,.35);line-height:1;
  }
  .headline--size{left:1020px;top:78px;font-size:128px;letter-spacing:-4px;}
  .headline--size small{font-size:88px;}
  .headline--role{left:1076px;top:204px;writing-mode:vertical-rl;font-size:86px;letter-spacing:-4px;}
  .headline--hire{left:962px;top:300px;writing-mode:vertical-rl;font-size:94px;letter-spacing:-4px;}
  .headline--hire small{font-size:68px;}
  .pay{
    position:absolute;left:0;top:636px;width:1200px;height:164px;
    background:linear-gradient(180deg,var(--navy) 0%,var(--navy-dark) 100%);
    display:flex;align-items:center;justify-content:center;
  }
  .pay-text{
    font-family:"Shippori Mincho B1",serif;font-weight:800;font-size:72px;
    background:linear-gradient(180deg,#fff3b8 0%,var(--gold) 45%,var(--gold-deep) 100%);
    -webkit-background-clip:text;background-clip:text;color:transparent;
    letter-spacing:2px;line-height:1;
  }
  .pay-text .num{font-size:124px;}
</style>
</head>
<body>
<div class="banner">
  <div class="photo" role="img" aria-label="トラックの前で親指を立てる二人のドライバーの写真"></div>

  <div class="pill pill--route">固定ルート</div>
  <div class="op op--plus1">＋</div>
  <div class="pill pill--stamina">体力負担なし</div>
  <div class="op op--plus2">＋</div>
  <div class="pill pill--culture">無理な運転は<br>させない社風</div>
  <div class="op op--eq">＝</div>

  <svg class="bubble" viewBox="0 0 1200 800" aria-hidden="true">
    <path d="M448 444 H520 L538 318 L604 444 H640 L678 318 L700 444 H912 Q940 444 940 472 V582 Q940 610 912 610 H448 Q420 610 420 582 V472 Q420 444 448 444 Z"
          fill="#fff" stroke="#333" stroke-width="3" stroke-linejoin="round"/>
  </svg>
  <div class="bubble-text"><span>長く働ける</span><span>環境です！</span></div>

  <div class="headline headline--size">6<small>t</small></div>
  <div class="headline headline--role">ドライバー</div>
  <div class="headline headline--hire">募集<small>!!</small></div>

  <div class="pay"><div class="pay-text">月給<span class="num">35</span>万円可能</div></div>
</div>
</body>
</html>
```